Fun, challenging, and inspirational guide for life change - written by a coach, therapist and founde

I need (1) cover design for a book titled:
"THE WANDERER'S TOOLKIT FOR MIND-SHIFTING IDEAS" - the surprisingly practical magic of believing and taking action

A 2ND COVER will be need for a companion ebook, titled:
"THE HEARTH LEDGER FOR PURPOSE AND CONTENTMENT - 3 steps to help unlock and unleash the unlimited you by loving your limitations

These books will be used to promote a larger suite of products and services devoted to empowering and inspiring a community of OVERCOMERS.

For reference check out www.brightquillpath.com

I've included some photos for visual reference points.

DESIGNS CONCEPTS:
CLEAN - A BLEND OF PAST AND PRESENT - MODERN AND THE SACRED) (...The Marlowe's Atlas meets

Target Market(s)

young and aspiring professionals and seasoned pros looking for life-changes due to feeling unfulfilled in their profession and relationships

Industry/Entity Type

Life Coaching

Font styles to use
Serif
Sans Serif

Requirements
Must have
• CREATIVITY - ORIGINALITY - WICKEDLY CLEAN DESIGN- AND IMPACTFUL TRANSLATION OF BRAND CONCEPT - COLOR AND PUNCH
Nice to have
• I included some photos as reference point - **PLEASE SEE THE PHOTOS FOR THE STAR-GAZERS DESIGNS** - I really like the feeling they provoke - I want to give the viewer a sense of the journey that can be taken when they dive into these books.
• Basically, riff off the design profiles and colors included in the STAR-GAZER covers.
• MUSTS INCLUDE -
• -ORIGINALITY
• - IMPACT
• - COLOR
• - ORIGINAL DESIGNS+
• +
Should not have
• STAY AWAY FROM...
• 1 OVERUSED AND TRENDY ICONS
• - ESOTERIC IMAGES
• - FLOWERY SCRIPTS
• - I AM REALLY LOOKING FOR A UPDATE OF THE TYPICAL SELF-HELP BOOK COVERS WHICH RELY TOO MUCH ON FLOWERY AND SACRED IMAGERY
• THANK YOU - feel free to unleash your creativity!

```html
<!DOCTYPE html>
<html lang="en">
<head>
<meta charset="utf-8">
<title>The Wanderer's Toolkit for Mind-Shifting Ideas</title>
<link rel="stylesheet" href="https://fonts.googleapis.com/css2?family=Bebas+Neue&family=Oswald:wght@200;300&display=swap">
<style>
  :root {
    --sky-top: #1c2a78;
    --sky-mid: #3c3f92;
    --sky-bottom: #7c68a8;
    --ink: #ffffff;
    --emblem-light: #f4f2fb;
    --emblem-shade: #d9d4ee;
  }
  * { margin: 0; padding: 0; box-sizing: border-box; }
  html, body { width: 800px; height: 1200px; overflow: hidden; }
  body { background: var(--sky-top); }
  .cover {
    position: relative;
    width: 800px;
    height: 1200px;
    overflow: hidden;
    color: var(--ink);
    background: linear-gradient(180deg, var(--sky-top) 0%, var(--sky-mid) 45%, var(--sky-bottom) 100%);
    text-align: center;
  }
  .title { position: absolute; left: 0; right: 0; top: 52px; }
  .title span {
    display: block;
    font-family: "Bebas Neue", "Oswald", sans-serif;
    line-height: 0.92;
    white-space: nowrap;
  }
  .title-lead { font-size: 132px; letter-spacing: 4px; }
  .title-main { font-size: 112px; letter-spacing: 5px; margin-top: 14px; }
  .title-tail { font-size: 60px; letter-spacing: 1px; margin-top: 24px; }
  .subtitle {
    position: absolute; left: 0; right: 0; top: 462px;
    font-family: "Oswald", sans-serif;
    font-weight: 300;
    font-size: 23px;
    line-height: 37px;
    letter-spacing: 1.5px;
  }
  .emblem { position: absolute; left: 184px; top: 560px; width: 432px; height: 432px; }
  .author {
    position: absolute; left: 0; right: 0; top: 1052px;
    font-family: "Oswald", sans-serif;
    font-weight: 200;
    font-size: 96px;
    line-height: 1;
    letter-spacing: 14px;
    padding-left: 14px;
  }
</style>
</head>
<body>
  <main class="cover">
    <h1 class="title">
      <span class="title-lead">THE WANDERER'S</span>
      <span class="title-main">TOOLKIT</span>
      <span class="title-tail">FOR MIND-SHIFTING IDEAS</span>
    </h1>
    <p class="subtitle">11 BELIEFS TO UNLOCK AND UNLEASH YOUR<br>PASSION AND PURPOSE ON THE WORLD</p>
    <svg class="emblem" viewBox="0 0 432 432" role="img" aria-label="Emblem: a figure with a raised fist standing on a cliff edge before radiating light rays, inside a circle">
      <defs>
        <radialGradient id="emblemFill" cx="50%" cy="40%" r="60%">
          <stop offset="0%" stop-color="var(--emblem-light)"/>
          <stop offset="100%" stop-color="var(--emblem-shade)"/>
        </radialGradient>
      </defs>
      <circle cx="216" cy="216" r="210" fill="none" stroke="var(--ink)" stroke-width="6"/>
      <circle cx="216" cy="216" r="198" fill="url(#emblemFill)"/>
    </svg>
    <p class="author">AUTHOR NAME</p>
  </main>
</body>
</html>
```